Boston area Multi-store hair salon needs a poster for a special service

We need a poster for a soon to be multi-store hair salon based in the Boston area. We are expanding, opening more salons. We need a poster for a service we offer called "The Full Trim!" It is for men, and it includes:
1. Haircut
2. Shampoo
3. Neck Shave
4. Hot Towel Service

We charge $22 for The Full Trim!
70% of our clients are men.
Our website is www.mavenshears.example
Our colors are black and red
***Please focus on the "The Full Trim!" part of the poster. We are almost looking for logo or icon for The Full Trim! part. *****
This will be hung inside the store near the reception area and possibly through out the salon and could be included in emails.
I have attached our logo and some other branding items we use (business cards, rewards cards, envelopes, etc) to help give you an idea of the look and feel we currently have. I have also attached an ad from Halvern which is a coupon they use for a service they call the full trim, just to give an idea. We like how Halvern created "The Full Trim" as an icon or logo.

Target Market(s)

Men

Industry/Entity Type

Store

Requirements
Nice to have
• Pictures of each service. We uploaded some examples.
• Also, "The Full Trim!" should be like a logo/icon

```html
<!DOCTYPE html>
<html lang="en">
<head>
<meta charset="UTF-8">
<title>The Full Trim! — Maven Shears</title>
<link rel="stylesheet" href="https://fonts.googleapis.com/css2?family=Bebas+Neue&family=Oswald:wght@500;700&display=swap">
<style>
  :root {
    --red: #c8141b;
    --red-deep: #7d080c;
    --red-dark: #4a0406;
    --black: #111111;
    --white: #ffffff;
    --steel-light: #d9d9d9;
    --steel-mid: #8a8a8a;
    --steel-dark: #3b3b3b;
    --grey-swoosh: #b9b9b9;
  }
  * { margin: 0; padding: 0; box-sizing: border-box; }
  html, body { width: 900px; height: 1200px; overflow: hidden; background: var(--red-dark); }

  .poster {
    position: relative;
    width: 900px;
    height: 1200px;
    overflow: hidden;
    background: radial-gradient(ellipse at 35% 40%, var(--red) 0%, var(--red-deep) 60%, var(--red-dark) 100%);
    font-family: "Oswald", sans-serif;
  }

  .backdrop-photo {
    position: absolute;
    left: 60px; top: 380px;
    width: 620px; height: 680px;
    border-radius: 45% 45% 10% 10%;
    background: radial-gradient(ellipse at 50% 40%, rgba(0,0,0,0.22) 0%, rgba(0,0,0,0.08) 55%, rgba(0,0,0,0) 75%);
  }

  .title {
    position: absolute;
    left: 40px; top: 40px;
    width: 660px;
    text-align: center;
    font-family: "Bebas Neue", sans-serif;
    line-height: 0.86;
    background: linear-gradient(180deg, var(--steel-light) 0%, var(--steel-mid) 48%, var(--steel-dark) 52%, var(--steel-mid) 100%);
    -webkit-background-clip: text;
    background-clip: text;
    color: transparent;
    filter: drop-shadow(0 6px 6px rgba(0,0,0,0.55));
  }
  .title-the { display: block; font-size: 190px; letter-spacing: 4px; }
  .title-name { display: block; font-size: 200px; letter-spacing: 2px; }

  .price-block {
    position: absolute;
    left: 60px; top: 470px;
    width: 330px; height: 320px;
    color: var(--white);
  }
  .price-frame { position: absolute; inset: 0; }
  .price-amount {
    position: absolute;
    left: 40px; top: 30px;
    font-family: "Bebas Neue", sans-serif;
    font-size: 170px;
    line-height: 1;
  }
  .price-charge {
    position: absolute;
    left: 40px; top: 190px;
    font-family: "Bebas Neue", sans-serif;
    font-size: 84px;
    line-height: 1;
  }
  .price-note {
    position: absolute;
    left: 42px; top: 272px;
    font-weight: 500;
    font-size: 24px;
    letter-spacing: 1px;
  }

  .service-rail {
    position: absolute;
    left: 806px; top: 0;
    width: 8px; height: 1100px;
    background: var(--black);
    opacity: 0.55;
  }
  .service-photo {
    position: absolute;
    width: 180px; height: 180px;
    left: 720px;
    border-radius: 50%;
    border: 6px solid var(--white);
    box-shadow: 0 4px 10px rgba(0,0,0,0.5);
  }
  .photo-haircut { top: 10px;  background: radial-gradient(circle at 40% 40%, #e9e4df, #9b8f86); }
  .photo-shampoo { top: 255px; background: radial-gradient(circle at 45% 45%, #f2f2f2, #a6a09b); }
  .photo-shave   { top: 505px; background: radial-gradient(circle at 50% 45%, #d7c2b3, #7c6a60); }
  .photo-towel   { top: 755px; background: radial-gradient(circle at 50% 50%, #ffffff, #b8b8b8); }

  .service-tag {
    position: absolute;
    left: 700px;
    width: 210px; height: 58px;
    background: var(--white);
    color: var(--black);
    clip-path: polygon(0 0, 100% 0, 100% 100%, 0 100%, 12% 50%);
    transform: rotate(-5deg);
    display: flex;
    align-items: center;
    justify-content: center;
    padding-left: 20px;
    font-family: "Bebas Neue", sans-serif;
    font-size: 40px;
    letter-spacing: 2px;
    box-shadow: 0 3px 6px rgba(0,0,0,0.4);
  }
  .tag-haircut { top: 198px; }
  .tag-shampoo { top: 446px; }
  .tag-shave   { top: 694px; }
  .tag-towel   { top: 944px; }

  .footer-band { position: absolute; left: 0; top: 940px; width: 900px; height: 260px; }

  .brand {
    position: absolute;
    left: 14px; top: 955px;
    width: 160px; height: 160px;
    border-radius: 50%;
    background: var(--black);
    display: flex;
    align-items: center;
    justify-content: center;
    text-align: center;
    color: var(--white);
    font-family: "Bebas Neue", sans-serif;
    font-size: 40px;
    line-height: 0.95;
  }

  .website {
    position: absolute;
    left: 220px; top: 1110px;
    width: 520px;
    text-align: center;
    font-family: "Oswald", sans-serif;
    font-weight: 700;
    font-size: 40px;
    color: var(--black);
    letter-spacing: 1px;
  }
</style>
</head>
<body>
  <main class="poster">
    <div class="backdrop-photo" role="img" aria-label="Faint photo of a man having his hair styled"></div>

    <h1 class="title">
      <span class="title-the">The</span>
      <span class="title-name">Full Trim</span>
    </h1>

    <section class="price-block">
      <svg class="price-frame" width="330" height="320" viewBox="0 0 330 320">
        <polyline points="90,4 4,4 4,316" fill="none" stroke="#ffffff" stroke-width="6"/>
        <polyline points="240,316 326,316 326,230" fill="none" stroke="#ffffff" stroke-width="6"/>
      </svg>
      <div class="price-amount">$22</div>
      <div class="price-charge">Charge</div>
      <div class="price-note">FOR THE FULL TRIM</div>
    </section>

    <div class="service-rail"></div>

    <div class="service-photo photo-haircut" role="img" aria-label="Photo of a man getting a haircut"></div>
    <div class="service-tag tag-haircut">Haircut</div>

    <div class="service-photo photo-shampoo" role="img" aria-label="Photo of a shampoo wash at the sink"></div>
    <div class="service-tag tag-shampoo">Shampoo</div>

    <div class="service-photo photo-shave" role="img" aria-label="Photo of a razor neck shave"></div>
    <div class="service-tag tag-shave">Neck Shave</div>

    <div class="service-photo photo-towel" role="img" aria-label="Photo of a hot towel wrapped face"></div>
    <div class="service-tag tag-towel">Hot Towel</div>

    <svg class="footer-band" width="900" height="260" viewBox="0 0 900 260">
      <path d="M0 120 C250 60 560 150 900 60 L900 80 C560 170 250 90 0 150 Z" fill="var(--grey-swoosh)"/>
      <path d="M0 150 C250 90 560 170 900 80 L900 260 L0 260 Z" fill="#ffffff"/>
    </svg>

    <div class="brand">MAVEN<br>SHEARS</div>

    <div class="website">www.mavenshears.example</div>
  </main>
</body>
</html>
```